I need a banner ad for a Tee Shirt campaign. I will be promoting "Hats Off Quentin" T-shirts. This will be targeted to College Students and Vortexa Fans. I will not be advertising on ZW so I will not have to worry about Censorship. These are a couple of samples of the type of shirts.

```html
<!DOCTYPE html>
<html lang="en">
<head>
<meta charset="utf-8">
<title>Hats Off Quentin – Tee Campaign Banner</title>
<link href="https://fonts.googleapis.com/css2?family=Anton&family=Russo+One&display=swap" rel="stylesheet">
<style>
  :root {
    --sky-top: #8fc6ec;
    --sky-mid: #eaf4fb;
    --blush: #f3c4c9;
    --rose: #e0707a;
    --navy: #14237a;
    --flag-blue: #1f3f8f;
    --flag-red: #d9121f;
    --white: #ffffff;
    --shirt: #141414;
    --shirt-edge: #2a2a2a;
  }
  html, body {
    margin: 0;
    padding: 0;
    width: 1200px;
    height: 600px;
    overflow: hidden;
    background: var(--white);
  }
  .banner {
    position: relative;
    width: 1200px;
    height: 600px;
    overflow: hidden;
  }
  .banner-art {
    display: block;
    width: 1200px;
    height: 600px;
  }
  .headline-word {
    font-family: "Anton", "Impact", sans-serif;
  }
  .headline-name {
    font-family: "Russo One", "Arial Black", sans-serif;
  }
</style>
</head>
<body>
<main class="banner">
  <svg class="banner-art" viewBox="0 0 1200 600" xmlns="http://www.w3.org/2000/svg">
    <defs>
      <linearGradient id="sky" x1="0" y1="0" x2="0" y2="1">
        <stop offset="0" stop-color="var(--sky-top)"/>
        <stop offset="0.42" stop-color="var(--sky-mid)"/>
        <stop offset="0.75" stop-color="var(--blush)"/>
        <stop offset="1" stop-color="var(--rose)"/>
      </linearGradient>
      <linearGradient id="sweep" x1="0" y1="0" x2="1" y2="0">
        <stop offset="0" stop-color="#5aa7e0" stop-opacity="0.7"/>
        <stop offset="1" stop-color="#5aa7e0" stop-opacity="0"/>
      </linearGradient>
      <linearGradient id="hollow" x1="0" y1="0" x2="0" y2="1">
        <stop offset="0" stop-color="#ffffff" stop-opacity="0.9"/>
        <stop offset="1" stop-color="#ffffff" stop-opacity="0.35"/>
      </linearGradient>
    </defs>

    <rect class="backdrop" width="1200" height="600" fill="url(#sky)"/>
    <path class="backdrop-sweep" d="M0 40 C260 -20 520 80 820 20 L820 0 L0 0 Z" fill="url(#sweep)"/>

    <g class="ribbon">
      <path d="M0 255 C120 240 260 215 380 225 C480 232 560 230 650 215 L650 248 C560 262 480 262 380 258 C260 252 120 280 0 300 Z" fill="var(--flag-blue)"/>
      <path d="M0 300 C120 280 260 252 380 258 C480 262 560 262 650 248 L650 262 C560 280 480 285 380 285 C260 285 120 312 0 332 Z" fill="var(--white)"/>
      <path d="M0 332 C120 312 260 285 380 285 C480 285 560 280 650 262 L650 276 C560 300 480 308 380 310 C260 314 120 345 0 368 Z" fill="var(--flag-red)"/>
    </g>

    <text class="headline-word" x="85" y="213" textLength="420" lengthAdjust="spacingAndGlyphs"
          font-size="205" fill="var(--navy)" stroke="var(--flag-red)" stroke-width="4" paint-order="stroke">HATS</text>
    <text class="headline-word" x="95" y="395" textLength="320" lengthAdjust="spacingAndGlyphs"
          font-size="190" fill="url(#hollow)" stroke="var(--flag-red)" stroke-width="4">OFF</text>

    <g class="shirt-samples">
      <rect x="678" y="20" width="228" height="235" rx="10" fill="var(--shirt)" stroke="var(--shirt-edge)"
            role="img" aria-label="Black t-shirt printed with 'Hats Off Quentin' over a distressed flag"/>
      <rect x="865" y="15" width="315" height="225" rx="10" fill="var(--shirt)" stroke="var(--shirt-edge)"
            role="img" aria-label="Black t-shirt printed with 'Hats Off Quentin!' between red and blue star bands"/>
      <rect x="630" y="215" width="282" height="300" rx="10" fill="var(--shirt)" stroke="var(--shirt-edge)"
            role="img" aria-label="Black t-shirt printed with 'Hats Off Quentin!' between red and blue star bands"/>
      <rect x="880" y="235" width="265" height="280" rx="10" fill="var(--shirt)" stroke="var(--shirt-edge)"
            role="img" aria-label="Black t-shirt printed with 'Hats Off Quentin' over a distressed flag"/>
    </g>

    <text class="headline-name" x="72" y="560" textLength="1078" lengthAdjust="spacingAndGlyphs"
          font-size="118" fill="var(--flag-red)" stroke="var(--white)" stroke-width="8" paint-order="stroke">QUENTIN</text>
  </svg>
</main>
</body>
</html>
```